Powerpoint template & style design project

KLavender Consulting is an IT technology firm specializing in mobility and telecommunications applications. We provide technical consulting to global companies that want to build mobile applications and take critical business applications and move them into the cloud.
We would like to see designs that use the color blue. The final design should communicate confidence, agility and speak to technology focused customers. Forward progress and/or motion should be conveyed.

Target Market(s)

Government customers and large enterprise companies

Industry/Entity Type

Telecommunications

Font styles to use
Sans Serif

Colors
0555a3

Requirements
Must have
• different slides: Cover page, title slide, main content, transition slide, close out slide..

```html
<!DOCTYPE html>
<html lang="en">
<head>
<meta charset="utf-8">
<title>Project Title Here</title>
<link rel="stylesheet" href="https://fonts.googleapis.com/css2?family=Open+Sans:wght@400;600&family=Roboto+Condensed:wght@400&display=swap">
<style>
  :root {
    --brand-blue: #0b4f9c;
    --heading-blue: #0d4c94;
    --canvas-bg: #f2f2f2;
    --footer-band: #d1d1d1;
    --body-text: #555555;
    --white: #ffffff;
  }
  html, body {
    margin: 0;
    padding: 0;
    overflow: hidden;
  }
  .slide {
    position: relative;
    width: 1200px;
    height: 900px;
    background: var(--canvas-bg);
    overflow: hidden;
    font-family: "Open Sans", Arial, sans-serif;
  }
  .title-bar {
    position: absolute;
    left: 0;
    top: 0;
    width: 1200px;
    height: 93px;
    background: var(--brand-blue);
  }
  .slide-title {
    position: absolute;
    left: 29px;
    top: 12px;
    margin: 0;
    font-family: "Roboto Condensed", "Arial Narrow", sans-serif;
    font-weight: 400;
    font-size: 51px;
    line-height: 66px;
    color: var(--white);
    letter-spacing: -0.5px;
  }
  .brand-name {
    position: absolute;
    right: 24px;
    top: 30px;
    margin: 0;
    font-family: "Roboto Condensed", "Arial Narrow", sans-serif;
    font-weight: 400;
    font-size: 24px;
    line-height: 32px;
    color: var(--white);
  }
  .footer-band {
    position: absolute;
    left: 0;
    bottom: 0;
    width: 1200px;
    height: 42px;
    background: var(--footer-band);
  }
  .column {
    position: absolute;
    top: 172px;
    width: 530px;
  }
  .column--left { left: 44px; }
  .column--right { left: 620px; }
  .column-heading {
    margin: 0;
    height: 70px;
    font-weight: 600;
    font-size: 20px;
    line-height: 34px;
    color: var(--heading-blue);
    letter-spacing: -0.2px;
  }
  .column-text {
    position: absolute;
    left: 0;
    margin: 0;
    font-size: 17.5px;
    line-height: 33px;
    color: var(--body-text);
  }
  .column-text--first { top: 54px; }
  .column-text--second { top: 300px; }
  .column-text--third { top: 517px; }
</style>
</head>
<body>
<main class="slide">
  <header class="title-bar">
    <h1 class="slide-title">Project Title Here</h1>
    <p class="brand-name">KLavender Consulting</p>
  </header>

  <section class="column column--left">
    <h2 class="column-heading">Lorem ipsum dolor sit Lorem ipsum dolor</h2>
    <p class="column-text column-text--first">Lorem ipsum dolor sit Lorem ipsum dolor sit&nbsp; Lorem ipsum<br>dolor sit Lorem ipsum dolor sit&nbsp; Lorem ipsum dolor sit Lorem<br>ipsum dolor sit&nbsp; Lorem ipsum dolor sit Lorem ipsum dolor sit<br>Lorem ipsum dolor sit Lorem ipsum dolor sit&nbsp; Lorem ipsum<br>dolor sit Lorem ipsum dolor sit&nbsp; Lorem ipsum dolor sit Lorem<br>ipsum dolor sit&nbsp; Lorem ipsum dolor sit Lorem ipsum dolor sit</p>
    <p class="column-text column-text--second">Lorem ipsum dolor sit Lorem ipsum dolor sit&nbsp; Lorem ipsum<br>dolor sit Lorem ipsum dolor sit&nbsp; Lorem ipsum dolor sit Lorem<br>ipsum dolor sit&nbsp; Lorem ipsum dolor sit Lorem ipsum dolor sit<br>Lorem ipsum dolor sit</p>
    <p class="column-text column-text--third">Lorem ipsum dolor sit&nbsp; Lorem ipsum dolor sit Lorem ipsum<br>dolor sit&nbsp; Lorem ipsum dolor sit Lorem ipsum dolor sit&nbsp; Lorem<br>ipsum dolor sit Lorem ipsum dolor sit</p>
  </section>

  <section class="column column--right">
    <h2 class="column-heading">Lorem ipsum dolor sit Lorem ipsum dolor</h2>
    <p class="column-text column-text--first">Lorem ipsum dolor sit Lorem ipsum dolor sit&nbsp; Lorem ipsum<br>dolor sit Lorem ipsum dolor sit&nbsp; Lorem ipsum dolor sit Lorem<br>ipsum dolor sit&nbsp; Lorem ipsum dolor sit Lorem ipsum dolor sit<br>Lorem ipsum dolor sit Lorem ipsum dolor sit&nbsp; Lorem ipsum<br>dolor sit Lorem ipsum dolor sit&nbsp; Lorem ipsum dolor sit Lorem<br>ipsum dolor sit&nbsp; Lorem ipsum dolor sit Lorem ipsum dolor sit</p>
    <p class="column-text column-text--second">Lorem ipsum dolor sit Lorem ipsum dolor sit&nbsp; Lorem ipsum<br>dolor sit Lorem ipsum dolor sit&nbsp; Lorem ipsum dolor sit Lorem<br>ipsum dolor sit&nbsp; Lorem ipsum dolor sit Lorem ipsum dolor sit<br>Lorem ipsum dolor sit</p>
    <p class="column-text column-text--third">Lorem ipsum dolor sit&nbsp; Lorem ipsum dolor sit Lorem ipsum<br>dolor sit&nbsp; Lorem ipsum dolor sit Lorem ipsum dolor sit&nbsp; Lorem<br>ipsum dolor sit Lorem ipsum dolor sit</p>
  </section>

  <footer class="footer-band"></footer>
</main>
</body>
</html>
```